Brimvale OralNet IT Inc. new website

i need a website for my company which is dedicated to installation and service of computer systems in Dental Offices. I would like for it to encompass a technology feel and professional look. The company deals with all aspects of technology like, Audio Visual, computer systems and networks, Cloud services like data backup, data center. We provide manage services, support and services to Dental Professionals.

Looking for a Technology font but professional look Added Wednesday, April 20, 2016

Target Market(s)

Dental, Dentist

Industry/Entity Type

Dental

Number of Pages Required

5+ page

Font styles to use
Other font styles liked:
• Futuristic or Techy

Colors
0255a3
ec1f27

Requirements
Must have
• Tabs
Nice to have
• Have no idea maybe some suggestion on your part may help
Should not have
• A professional feel but have a techy look

```html
<!DOCTYPE html>
<html lang="en">
<head>
<meta charset="utf-8">
<title>Brimvale OralNet IT – About Us</title>
<link rel="stylesheet" href="https://fonts.googleapis.com/css2?family=Exo+2:wght@500;600;700&family=Lato:wght@400;700&family=Montserrat:wght@600;700&family=Oswald:wght@400&display=swap">
<style>
:root{
  --blue:#0255a3;
  --bar:#0a6fb8;
  --red:#ec1f27;
  --ink:#1c1c1c;
  --text:#2f2f2f;
  --footer:#2d2d2d;
  --footer-deep:#1d1d1d;
  --field:#1f1f1f;
  --muted:#c9c9c9;
}
*{box-sizing:border-box;margin:0;padding:0}
html,body{width:853px;height:1200px;overflow:hidden;background:#fff}
body{position:relative;font-family:"Lato",sans-serif;color:var(--text)}
.abs{position:absolute}

.topbar{left:0;top:0;width:853px;height:27px;background:var(--bar)}
.topbar .phone{left:562px;top:4px;font-family:"Oswald",sans-serif;font-size:14px;color:#fff;letter-spacing:.5px;display:flex;align-items:center;gap:6px}
.social{display:flex;gap:8px}
.social span{width:19px;height:19px;border-radius:3px;background:rgba(255,255,255,.85);border:1px solid #fff;display:block}
.topbar .social{left:687px;top:4px}

.header{left:0;top:27px;width:853px;height:82px;background:#fff}
.brand{left:94px;top:24px;display:flex;align-items:center;gap:8px;font-family:"Exo 2",sans-serif;font-weight:700;font-size:19px;color:var(--blue);line-height:1}
.brand i{width:26px;height:26px;background:var(--blue);border-radius:4px;display:block}
.nav{left:328px;top:30px;display:flex;align-items:center;font-family:"Montserrat",sans-serif;font-weight:700;font-size:11.5px;color:var(--ink)}
.nav a{color:inherit;text-decoration:none;padding:0 21px;border-left:1px solid #9cc3e4;line-height:14px}
.nav a:first-child{border:none;padding-left:0}
.nav a.active{color:var(--bar)}

.hero{left:0;top:109px;width:853px;height:213px;background:linear-gradient(90deg,#c4ccd6 0%,#8e9db3 25%,#3b5e8e 55%,#1f2a3c 80%,#2b2f36 100%)}
.hero .line1{left:221px;top:28px;font-family:"Exo 2",sans-serif;font-weight:700;font-size:27px;color:#fff}
.hero .box{left:342px;top:67px;width:479px;height:81px;border:1px solid rgba(255,255,255,.45);background:rgba(10,30,70,.35);display:flex;align-items:center;padding-left:18px;gap:8px}
.hero .box b{font-family:"Exo 2",sans-serif;font-weight:700;font-size:48px;color:#fff;margin-right:10px;letter-spacing:1px}
.hero .box i{width:57px;height:57px;border-radius:50%;border:3px solid #dde6f2;background:linear-gradient(#3f75b8,#173f78);display:block}
.hero .line3{left:362px;top:152px;font-family:"Exo 2",sans-serif;font-weight:700;font-size:27px;color:#fff}

.title{left:0;top:353px;width:853px;text-align:center;font-family:"Exo 2",sans-serif;font-weight:700;font-size:26px;color:var(--ink)}
.rule{left:267px;top:403px;width:319px;height:1px;background:#cfcfcf}
.rule-mark{left:420px;top:397px;width:14px;height:12px;background:#8a8a8a;border:2px solid #fff;border-radius:2px;outline:1px solid #bbb}

p.copy{font-size:11px;line-height:19.2px;letter-spacing:.15px;color:var(--text)}
.p1{left:94px;top:421px;width:666px}
.p2{left:348px;top:519px;width:412px}
.p3{left:94px;top:704px;width:412px}
.photo{width:234px;height:147px}
.photo1{left:94px;top:520px;background:linear-gradient(160deg,#dfe6f5,#9aa6c0 40%,#5b6f93 70%,#c7c1b6)}
.photo2{left:525px;top:706px;background:linear-gradient(120deg,#b3a290,#e9ecef 45%,#f4f6f8 60%,#6f7c8a)}

.footer{left:0;top:900px;width:853px;height:264px;background:var(--footer)}
.fh{font-family:"Exo 2",sans-serif;font-weight:600;font-size:14.5px;color:#fff;padding-bottom:10px;border-bottom:1px dotted #777}
.col-links{left:95px;top:929px;width:98px}
.col-contact{left:241px;top:929px;width:147px}
.col-inq{left:447px;top:929px;width:171px}
.vsep{top:968px;width:2px;height:150px;background:linear-gradient(transparent,#444,transparent)}
.links{list-style:none;margin-top:15px}
.links li{font-size:11px;color:#e6e6e6;height:30px;line-height:14px}
.links li::before{content:"›";margin-right:6px}
.links li.on{font-weight:700;color:#fff}
.contact{color:#eee;font-size:11px;line-height:14px}
.contact .row{position:absolute;left:0;display:flex;gap:10px}
.contact svg{flex:none}
.field{position:absolute;left:0;width:173px;height:20px;background:var(--field);color:#9a9a9a;font-size:10px;padding:4px 8px;border-radius:2px}
.submit{position:absolute;left:0;top:184px;width:68px;height:24px;background:var(--blue);color:#fff;font-weight:700;font-size:13px;text-align:center;line-height:24px}
.fbrand{left:660px;top:978px;width:110px;text-align:center;font-family:"Exo 2",sans-serif;font-weight:700;font-size:16px;color:#6a6a6a;line-height:1.15}
.fbrand i{display:block;width:30px;height:30px;background:#5a5a5a;border-radius:4px;margin:0 auto 8px}
.footer-social{left:677px;top:1083px}
.footer-social span{background:#8a8a8a;border-color:#aaa}
.bottombar{left:0;top:1164px;width:853px;height:36px;background:var(--footer-deep);color:#e0e0e0;font-size:10.5px;text-align:center;line-height:36px}
</style>
</head>
<body>

<div class="abs topbar">
  <div class="abs phone">
    <svg width="16" height="16" viewBox="0 0 16 16"><circle cx="8" cy="8" r="7" fill="none" stroke="#fff" stroke-width="1.3"/><path d="M5.3 4.6l1.3-.3.8 1.8-.9.7c.4.9 1.1 1.6 2 2l.7-.9 1.8.8-.3 1.3c-3.2.2-5.5-2.2-5.4-5.4z" fill="#fff"/></svg>
    555-013-2846
  </div>
  <div class="abs social" aria-label="Social links"><span></span><span></span><span></span></div>
</div>

<div class="abs header">
  <div class="abs brand"><i></i>Brimvale OralNet IT</div>
  <nav class="abs nav">
    <a href="#"><svg width="20" height="16" viewBox="0 0 20 16"><path d="M10 1L1 9h2.5v6h5v-4h3v4h5V9H19z" fill="#1c1c1c"/></svg></a>
    <a href="#" class="active">ABOUT US</a>
    <a href="#">SERVICES</a>
    <a href="#">SUPPORT</a>
    <a href="#">CONTACT US</a>
  </nav>
</div>

<section class="abs hero" role="img" aria-label="Dental treatment room with a blue patient chair beside an IT professional">
  <div class="abs line1">We Provide Manage Services,</div>
  <div class="abs box"><b>SUPPORT</b><i></i><i></i><i></i></div>
  <div class="abs line3">&amp; Service To Dental Professionals.</div>
</section>

<h1 class="abs title">About Us</h1>
<div class="abs rule"></div>
<div class="abs rule-mark"></div>

<p class="abs copy p1">Lorem ipsum dolor sit amet, consectetuer adipiscing elit, sed diam nonummy nibh euismod tincidunt ut laoreet dolore magna aliquam erat volutpat. Ut wisi enim ad minim veniam, quis nostrud exerci tation ullamcorper suscipit lobortis nisl ut aliquip ex ea commodo consequat. Duis autem vel eum iriure dolor in hendrerit in vulputate velit esse molestie consequat, vel illum dolore feugiat nulla facilisis at vero eros et accumsan et iusto odio dignissim qui blandit praesent luptatum zzril facilisi.</p>

<div class="abs photo photo1" role="img" aria-label="Modern dental clinic with blue chairs and ceiling lights"></div>
<p class="abs copy p2">Lorem ipsum dolor sit amet, consectetuer adipiscing elit, sed diam nonummy nibh euismod tincidunt ut laoreet dolore magna aliquam erat volutpat. Ut wisi enim ad minim veniam, quis nostrud exerci tation ullamcorper suscipit lobortis nisl ut aliquip ex ea commodo consequat. Duis autem vel eum iriure dolor in hendrerit in vulputate velit esse molestie consequat, vel illum dolore feugiat nulla facilisis at vero eros et accumsan et iusto odio dignissim qui blandit praesent luptatum zzril facilisi. Lorem ipsum dolor sit amet, consectetuer adipiscing elit, sed diam nonummy nibh euismod tincidunt ut laoreet dolore magna aliquam erat volutpat.</p>

<p class="abs copy p3">Lorem ipsum dolor sit amet, consectetuer adipiscing elit, sed diam nonummy nibh euismod tincidunt ut laoreet dolore magna aliquam erat volutpat. Ut wisi enim ad minim veniam, quis nostrud exerci tation ullamcorper suscipit lobortis nisl ut aliquip ex ea commodo consequat. Duis autem vel eum iriure dolor in hendrerit in vulputate velit esse molestie consequat, vel illum dolore feugiat nulla facilisis at vero eros et accumsan et iusto odio dignissim qui blandit praesent luptatum zzril facilisi. Lorem ipsum dolor sit amet, consectetuer adipiscing elit, sed diam nonummy nibh euismod tincidunt ut laoreet dolore magna aliquam erat volutpat.</p>
<div class="abs photo photo2" role="img" aria-label="Dentist reviewing a chart next to an x-ray monitor"></div>

<footer class="abs footer"></footer>
<div class="abs vsep" style="left:216px"></div>
<div class="abs vsep" style="left:422px"></div>
<div class="abs vsep" style="left:643px"></div>

<div class="abs col-links">
  <div class="fh">Quick Links</div>
  <ul class="links">
    <li class="on">Home</li><li>About Us</li><li>Services</li><li>Support</li><li>Contact Us</li>
  </ul>
</div>

<div class="abs col-contact contact">
  <div class="fh">Contact Details</div>
  <div class="row" style="top:50px">
    <svg width="10" height="13" viewBox="0 0 10 13"><path d="M5 0a4.5 4.5 0 0 0-4.5 4.5C.5 8 5 13 5 13s4.5-5 4.5-8.5A4.5 4.5 0 0 0 5 0zm0 6.3a1.8 1.8 0 1 1 0-3.6 1.8 1.8 0 0 1 0 3.6z" fill="#eee"/></svg>
    <div><b>Brimvale OralNet IT</b><br>2200 Harrowgate Ave – Suite 410<br>Brimvale, MN 55190</div>
  </div>
  <div class="row" style="top:122px;font-size:12px;font-weight:700">
    <svg width="11" height="12" viewBox="0 0 11 12"><path d="M1 1.5l2.4-.8 1.3 2.9-1.3 1c.6 1.4 1.6 2.4 3 3l1-1.3 2.9 1.3-.8 2.4C4.5 10.3.7 6.5 1 1.5z" fill="#eee"/></svg>
    555.013.2846
  </div>
  <div class="row" style="top:166px">
    <svg width="13" height="10" viewBox="0 0 13 10"><rect x=".5" y=".5" width="12" height="9" fill="none" stroke="#eee"/><path d="M.5.5l6 5 6-5" fill="none" stroke="#eee"/></svg>
    info@brimvaleoralnet.com
  </div>
</div>

<div class="abs col-inq">
  <div class="fh">Quick Inquiry</div>
  <div class="field" style="top:51px">Name</div>
  <div class="field" style="top:76px">Email</div>
  <div class="field" style="top:100px">Phone</div>
  <div class="field" style="top:125px;height:53px">Message</div>
  <div class="submit">SUBMIT</div>
</div>

<div class="abs fbrand"><i></i>Brimvale<br>OralNet IT</div>
<div class="abs social footer-social" aria-label="Social links"><span></span><span></span><span></span></div>

<div class="abs bottombar">copyright © 2016 Brimvale OralNet IT. ALL RIGHT RESERVED</div>

</body>
</html>
```